Lomi-Seret - Promote and Support a community

Design a website for Ethiopean Community. the design should be friendly, easy to navigate and maintain the look & feel of the Ethiopian culture. a proposed logo is attached but it can be change according to your recommendations. This is a project we are doing at a discount rate as it supports a weak community.
Please visit their current website http://www.lomi-seret.example.il/index.php?lang=en

Target Market(s)

Community members, potential doners

Industry/Entity Type

community

Number of Pages Required

1 page

Font styles to use
Sans Serif

Requirements
Must have
• easy to navigate friendly interface

```html
<!DOCTYPE html>
<html lang="en">
<head>
<meta charset="utf-8">
<title>Lomi-Seret</title>
<link href="https://fonts.googleapis.com/css2?family=Montserrat:wght@400;500;600;700;800&display=swap" rel="stylesheet">
<style>
:root{
  --green:#0f7a0c;
  --green-dark:#0b5e09;
  --green-deep:#1b6e33;
  --green-soft:#2a8a27;
  --ink:#1a1a1a;
  --text:#3a3a3a;
  --line:#b9dcc4;
  --footer:#1d1d1d;
  --white:#ffffff;
}
*{margin:0;padding:0;box-sizing:border-box}
html,body{width:1200px;height:4680px;overflow:hidden}
body{position:relative;background:var(--white);font-family:'Montserrat',sans-serif;color:var(--text)}
/* header */
.site-header{position:absolute;left:0;top:0;width:1200px;height:91px;background:var(--white);border-top:3px solid var(--green)}
.brand{position:absolute;left:102px;top:16px;display:flex;align-items:center;gap:8px}
.brand-mark{width:18px;height:18px;border-radius:50%;background:var(--green)}
.brand-name{font-weight:700;font-size:17px;color:var(--green)}
.main-nav{position:absolute;top:62px;left:268px;display:flex}
.main-nav a{font-size:13px;font-weight:500;color:#333;text-decoration:none;text-transform:uppercase;margin-right:38px}
.main-nav a.active{color:var(--green)}
.main-nav a:last-child{margin-right:0}
.btn-lang{position:absolute;left:749px;top:0;width:126px;height:46px;border:1.5px solid var(--green);border-top:0;border-radius:0 0 8px 8px;display:flex;align-items:center;justify-content:center;gap:10px;font-weight:700;font-size:15px;color:var(--green)}
.btn-contact{position:absolute;left:902px;top:0;width:185px;height:46px;background:var(--green);border-radius:0 0 8px 8px;display:flex;align-items:center;justify-content:center;gap:10px;font-weight:700;font-size:15px;color:var(--white)}
/* hero */
.hero{position:absolute;left:0;top:91px;width:1200px;height:600px}
.hero-photo{position:absolute;inset:0;background:linear-gradient(120deg,#6b4a2a 0%,#b77a3c 40%,#c9683e 60%,#8a3b2a 100%)}
.hero-title{position:absolute;left:115px;top:280px;font-size:34px;font-weight:600;color:var(--white);letter-spacing:.5px}
.hero-arrow{position:absolute;top:276px;width:54px;height:54px;border:2px solid var(--white);border-radius:50%;display:flex;align-items:center;justify-content:center}
.hero-dots{position:absolute;left:578px;top:553px;display:flex;gap:8px}
.hero-dots span{width:9px;height:9px;border-radius:50%;border:1.5px solid var(--white)}
.hero-dots span.on{background:var(--green);border-color:var(--green)}
.hero-curve{position:absolute;left:0;bottom:-1px}
/* shared */
.section-title{font-weight:800;color:var(--ink);text-transform:uppercase;font-size:34px;letter-spacing:.3px}
.btn{position:absolute;width:182px;height:44px;border-radius:22px 0 22px 0;display:flex;align-items:center;justify-content:center;font-weight:700;font-size:14px;letter-spacing:.5px;text-transform:uppercase}
.btn-green{background:var(--green);color:var(--white)}
.btn-white{background:var(--white);color:var(--green)}
.copy p{font-size:14.5px;line-height:26px;letter-spacing:-.1px}
.center{text-align:center}
/* welcome */
.welcome-title{position:absolute;left:0;width:1200px;top:765px;text-align:center}
.welcome-copy{position:absolute;left:125px;width:950px;top:830px}
.welcome-copy p+p{margin-top:26px}
.divider{position:absolute;left:111px;top:1246px;width:978px;height:2px;background:var(--line)}
.divider-knob{position:absolute;left:580px;top:1226px;width:40px;height:40px;border-radius:50%;background:var(--green);display:flex;align-items:center;justify-content:center}
/* about */
.about-visual{position:absolute;left:116px;top:1325px;width:430px;height:420px}
.about-title{position:absolute;left:584px;top:1325px}
.about-copy{position:absolute;left:584px;top:1390px;width:510px}
/* community band */
.community{position:absolute;left:0;top:1800px;width:1200px;height:720px}
.community-title{position:absolute;left:0;width:1200px;top:1935px;text-align:center;color:var(--white)}
.community-copy{position:absolute;left:115px;top:2013px;width:510px;color:var(--white)}
.community-copy p+p{margin-top:26px}
.community-photo{position:absolute;left:634px;top:2002px;width:453px;height:367px;border-radius:6px;background:linear-gradient(135deg,#5b6b55,#8b7a64 45%,#3f5870)}
.community-accent{position:absolute;background:var(--green-soft);border-radius:4px}
/* presentations */
.pres-title{position:absolute;left:0;width:1200px;top:2585px;text-align:center}
.pres-copy{position:absolute;left:130px;width:940px;top:2648px}
.pres-copy strong{color:var(--green);font-weight:600}
.pres-photo{position:absolute;left:220px;top:3022px;width:762px;height:391px;border:2px solid var(--green);border-radius:8px;background:linear-gradient(135deg,#3b3f48,#6c6e72 50%,#2c3b4d)}
/* advocacy */
.advocacy{position:absolute;left:0;top:3540px;width:1200px;height:440px}
.advocacy-title{position:absolute;left:0;width:1200px;top:3632px;text-align:center;color:var(--white)}
.advocacy-copy{position:absolute;left:125px;width:950px;top:3692px;color:var(--white)}
.advocacy-copy p+p{margin-top:24px}
/* partners */
.partner{position:absolute;top:4040px;background:#e4ece6;border-radius:8px}
/* footer */
.site-footer{position:absolute;left:0;top:4222px;width:1200px;height:458px}
.footer-brand{position:absolute;left:148px;top:4400px;width:180px;display:flex;align-items:center;gap:10px}
.footer-brand .brand-mark{width:22px;height:22px}
.footer-brand .brand-name{color:var(--white);font-size:22px}
.footer-col{position:absolute;top:4325px;color:var(--white)}
.footer-col h4{font-size:17px;font-weight:700;text-transform:uppercase}
.footer-col .rule{width:44px;height:3px;background:var(--green);margin:12px 0 16px}
.footer-col ul{list-style:none}
.footer-col li{font-size:11.5px;line-height:24px;text-transform:uppercase}
.contact-item{display:flex;gap:14px;align-items:center;margin-bottom:18px}
.contact-icon{width:34px;height:34px;border-radius:50%;border:1.5px solid #888;display:flex;align-items:center;justify-content:center}
.contact-item small{display:block;font-size:10.5px;text-transform:uppercase;color:#bbb}
.contact-item span{font-size:15px}
.footer-rule{position:absolute;left:111px;top:4611px;width:978px;height:1px;background:var(--green)}
.copyright{position:absolute;left:0;width:1200px;top:4643px;text-align:center;font-size:12px;color:var(--white)}
.to-top{position:absolute;left:1124px;top:4600px;width:42px;height:42px;border-radius:50%;background:var(--green);display:flex;align-items:center;justify-content:center}
</style>
</head>
<body>

<header class="site-header">
  <div class="brand"><span class="brand-mark"></span><span class="brand-name">Lomi-Seret</span></div>
  <nav class="main-nav">
    <a class="active">Home</a><a>About</a><a>The Community</a><a>Programs</a><a>News</a><a>Advocacy</a><a>Partners</a><a>Support Us</a>
  </nav>
  <div class="btn-lang">
    <svg width="22" height="22" viewBox="0 0 24 24" fill="none" stroke="#0f7a0c" stroke-width="1.8"><circle cx="12" cy="12" r="10"/><path d="M2 12h20M12 2c3 3 3 17 0 20M12 2c-3 3-3 17 0 20"/></svg>ABRIT
  </div>
  <div class="btn-contact">
    <svg width="18" height="18" viewBox="0 0 24 24" fill="#fff"><path d="M6.6 10.8a15 15 0 0 0 6.6 6.6l2.2-2.2c.3-.3.7-.4 1-.2 1.1.4 2.3.6 3.6.6.6 0 1 .4 1 1V20c0 .6-.4 1-1 1A17 17 0 0 1 3 4c0-.6.4-1 1-1h3.5c.6 0 1 .4 1 1 0 1.3.2 2.5.6 3.6.1.3 0 .7-.2 1z"/></svg>CONTACT US
  </div>
</header>

<section class="hero">
  <div class="hero-photo" role="img" aria-label="Smiling girl carrying a woven basket on her head"></div>
  <div class="hero-arrow" style="left:32px"><svg width="22" height="22" viewBox="0 0 24 24" fill="none" stroke="#fff" stroke-width="2"><path d="M20 12H4M10 6l-6 6 6 6"/></svg></div>
  <div class="hero-arrow" style="left:1112px"><svg width="22" height="22" viewBox="0 0 24 24" fill="none" stroke="#fff" stroke-width="2"><path d="M4 12h16M14 6l6 6-6 6"/></svg></div>
  <h1 class="hero-title">WELCOME TO LOMI-SERET</h1>
  <div class="hero-dots"><span class="on"></span><span></span><span></span></div>
  <svg class="hero-curve" width="1200" height="70" viewBox="0 0 1200 70"><path d="M0 10 Q600 60 1200 0 L1200 70 L0 70Z" fill="#fff"/></svg>
</section>

<h2 class="section-title welcome-title">Welcome to Lomi Seret</h2>
<div class="copy welcome-copy center">
  <p>Aliyah (immigration) from Ethiopia to Israel and the transition to a sedentary lifestyle has resulted in the emergence of chronic diseases, in particular diabetes. While only 0.4% of the new immigrants were diagnosed with Type 2 diabetes upon arrival, by the time they had lived in Israel for ten years the figure had risen to 18% - three times as many as in the general population.  The incidence of hypertension, obesity, asthma and Type 1 diabetes had also increased dramatically.</p>
  <p>Lomi Seret was founded in 1999 by Dr. Miriam Dovev, Head of the Endocrinology Unit at the Carmel Ridge Medical Center. Her experience with Ethiopian patients made her realize that medical treatment could not succeed without culturally competent communication.  Lomi Seret has developed into a small but dedicated NGO, delivering services throughout Israel with the backing and cooperation of a wide range of local and national bodies, including the Ministry of Health, the Ministry of Immigration, the absorption services, municipalities, the HMOs and hospitals.</p>
</div>
<div class="btn btn-green" style="left:509px;top:1115px">Learn More</div>

<div class="divider"></div>
<div class="divider-knob"><svg width="18" height="18" viewBox="0 0 24 24" fill="none" stroke="#fff" stroke-width="3"><path d="M6 9l6 6 6-6"/></svg></div>

<div class="about-visual">
  <svg width="430" height="420" viewBox="0 0 430 420">
    <circle cx="210" cy="205" r="205" fill="var(--green-deep)"/>
    <circle cx="240" cy="204" r="186" fill="#fff"/>
  </svg>
  <div role="img" aria-label="Three young children standing together outside a doorway" style="position:absolute;left:74px;top:32px;width:346px;height:346px;border-radius:50%;background:linear-gradient(135deg,#c9c2b0,#7a6a5a 50%,#b03a3a)"></div>
</div>
<h2 class="section-title about-title">About Lomi Seret</h2>
<div class="copy about-copy"><p>A 12-year-old girl from an Ethiopian immigrant family presented at the emergency department of the Carmel Ridge Medical Center. She was suffering from severe abdominal pains, and the tests showed that her glucose levels were extremely high, but although the staff explained to her family how serious her condition was, she did not return for treatment. The interpreter – herself a member of the Ethiopian immigrant community – who was brought in to facilitate communication with the young patient's parents did not understand.</p></div>
<div class="btn btn-green" style="left:584px;top:1645px">Learn More</div>

<svg class="community" viewBox="0 0 1200 720" preserveAspectRatio="none"><path d="M0 110 Q600 -50 1200 110 L1200 660 Q600 770 0 660Z" fill="var(--green)"/></svg>
<h2 class="section-title community-title">Health &amp; the Ethiopian Israeli Community</h2>
<div class="copy community-copy">
  <p>Today the Ethiopian Israeli community numbers over 120,000 with new immigrants still continuing to arrive. For many, immigration led to the disintegration of traditional family and social structures with traumatic results for the community and further impeding absorption into Israeli society.</p>
  <p>A report issued in 2008 by the Prime Minister's Office states that 68% of Ethiopian families live under the poverty line and the Tzedek Policy Centre advises that "Ethiopian immigrants ranked lowest on the quality of life index, which considers per-capita income, per-room housing density and basic spending". A study on the</p>
</div>
<div class="btn btn-white" style="left:115px;top:2322px">Learn More</div>
<div class="community-accent" role="img" aria-label="Decorative accent block" style="left:1096px;top:2254px;width:76px;height:112px"></div>
<div class="community-accent" role="img" aria-label="Decorative accent block" style="left:838px;top:2374px;width:334px;height:60px"></div>
<div class="community-photo" role="img" aria-label="Young students sitting together outdoors reading notes"></div>

<h2 class="section-title pres-title">Health &amp; Education Presentations</h2>
<div class="copy pres-copy center"><p><strong>To spread awareness of a health promoting lifestyle and an understanding of diabetes</strong> and other "lifestyle" chronic diseases, the team of Lomi Seret lecturers deliver presentations to the Ethiopian-Israeli community in Amharic through community centers and clinics, absorption centers, hostels for the elderly, etc.  The presentations have a visual component and the presenter encourages the audience to interact by asking questions and discussing concerns arising from traditional health beliefs or poor understanding.  Most locations receive a series of lectures covering a range of health topics relevant to the community.  Part of Lomi Seret's unique approach has been to design a presentation on the importance of physical activity – this lecture is delivered by qualified physical exercise instructors, and uses Ethiopian music and traditional dance movements to help promote regular physical activity as a lifestyle change.  Lomi Seret involves local leaders to provide credibility and influence to their message of health promotion, and conclude meetings with glucose screenings for the audience.  In 2009, over 290 presentations were delivered with an average audience of between 18 to 25 people.</p></div>
<div class="btn btn-green" style="left:509px;top:2958px">Learn More</div>
<div class="pres-photo" role="img" aria-label="Group of professionals in a meeting around a table with a laptop"></div>

<svg class="advocacy" viewBox="0 0 1200 440" preserveAspectRatio="none"><defs><linearGradient id="ag" x1="0" y1="0" x2="0" y2="1"><stop offset="0" stop-color="#146b14"/><stop offset="1" stop-color="#0f5e0e"/></linearGradient></defs><path d="M0 20 Q600 -20 1200 20 L1200 410 Q600 460 0 410Z" fill="url(#ag)"/></svg>
<h2 class="section-title advocacy-title">Advocacy</h2>
<div class="copy advocacy-copy center">
  <p>To advocate the unique needs of the community Lomi Seret pressures members of the Knesset, the Departments of Health, Social Welfare and Absorption, and the National Insurance Institute to adopt measures that will improve the circumstances of the Ethiopian-Israeli community and eliminate existing health disparities.</p>
  <p>Lomi Seret routinely delivers presentations to key people in the Israeli healthcare system to ensure they are kept aware of the recent findings and results of Lomi Seret's activities.</p>
</div>

<div class="partner" style="left:150px;width:130px;height:120px"></div>
<div class="partner" style="left:390px;width:130px;height:70px;top:4065px"></div>
<div class="partner" style="left:590px;width:120px;height:90px;top:4055px"></div>
<div class="partner" style="left:795px;width:130px;height:90px;top:4055px"></div>
<div class="partner" style="left:995px;width:80px;height:120px"></div>

<svg class="site-footer" viewBox="0 0 1200 458" preserveAspectRatio="none"><path d="M0 60 Q600 -40 1200 60 L1200 458 L0 458Z" fill="var(--footer)"/></svg>
<div class="footer-brand"><span class="brand-mark"></span><span class="brand-name">Lomi-Seret</span></div>
<div class="footer-col" style="left:384px"><h4>Quick Links</h4><div class="rule"></div><ul><li>Home</li><li>About</li><li>The Community</li><li>Programs</li><li>News</li><li>Advocacy</li><li>Partners</li><li>Support Us</li></ul></div>
<div class="footer-col" style="left:571px"><h4>Links</h4><div class="rule"></div><ul><li>Copyright</li><li>Legal</li><li>Privacy</li><li>Accessibility</li><li>Sitemap</li></ul></div>
<div class="footer-col" style="left:716px"><h4>Contact Us</h4><div class="rule"></div>
  <div class="contact-item"><div class="contact-icon"><svg width="16" height="16" viewBox="0 0 24 24" fill="#fff"><path d="M6.6 10.8a15 15 0 0 0 6.6 6.6l2.2-2.2c.3-.3.7-.4 1-.2 1.1.4 2.3.6 3.6.6.6 0 1 .4 1 1V20c0 .6-.4 1-1 1A17 17 0 0 1 3 4c0-.6.4-1 1-1h3.5c.6 0 1 .4 1 1 0 1.3.2 2.5.6 3.6.1.3 0 .7-.2 1z"/></svg></div><div><small>Phone</small><span>04-5550192</span></div></div>
  <div class="contact-item"><div class="contact-icon"><svg width="16" height="16" viewBox="0 0 24 24" fill="none" stroke="#fff" stroke-width="2"><path d="M12 22s7-7 7-12a7 7 0 0 0-14 0c0 5 7 12 7 12z"/><circle cx="12" cy="10" r="2.5"/></svg></div><div><small>Office</small><span>Hadas 12/4 POB 2210 Givat Ora, 38990</span></div></div>
  <div class="contact-item"><div class="contact-icon"><svg width="16" height="16" viewBox="0 0 24 24" fill="none" stroke="#fff" stroke-width="2"><rect x="3" y="5" width="18" height="14" rx="2"/><path d="M3 7l9 6 9-6"/></svg></div><div><small>Email</small><span>hello@lomi-seret.example.il</span></div></div>
</div>
<div class="footer-rule"></div>
<div class="copyright">©2022 All rights reserved.</div>
<div class="to-top"><svg width="16" height="16" viewBox="0 0 24 24" fill="none" stroke="#fff" stroke-width="3"><path d="M6 15l6-6 6 6"/></svg></div>

</body>
</html>
```